Business Card Design Project

Hello Designers, hope you are all aiming enjoy the weekend
I have the Business Logo (uploaded), you can alter the color which ever way you think would work,
Im looking for a simple yet striking feel, something which will stay memorable (I have uploaded 3 examples for you to flick through)
Information on the card, will just be the bare minimum,
Double Sided
Info being
i.e.
Name
Number
Website
ABN
Tobin Wexmoor
+468213579 (singapore)
+315792846 (Australia)
+729384615 (America)
www.lomevu-linkup.example
ABN 86420913
Enjoy,
Tobin
Industry/Entity Type
Business
Look and feel
Each slider illustrates characteristics of the customer's brand and the style your logo design should communicate.

```html
<!DOCTYPE html>
<html lang="en">
<head>
<meta charset="utf-8">
<title>Lomevu Linkup — Business Card</title>
<link rel="stylesheet" href="https://fonts.googleapis.com/css2?family=Arimo:wght@400;700&family=Quicksand:wght@500&display=swap">
<style>
  :root {
    --backdrop: #e6e6e6;
    --card-front: #b8c8d3;
    --card-back: #2b2523;
    --strip: #a9bccb;
    --brand-grey: #626366;
    --brand-red: #c9203f;
    --ink-light: #ffffff;
    --rule: #8c8c8c;
  }
  * { box-sizing: border-box; margin: 0; padding: 0; }
  html, body {
    width: 1200px; height: 951px; overflow: hidden;
    background: var(--backdrop);
  }
  .canvas { position: relative; width: 1200px; height: 951px; }

  .card {
    position: absolute;
    width: 560px; height: 320px;
    box-shadow: 0 6px 18px rgba(0,0,0,0.25);
  }

  /* Front side */
  .card-front { left: 90px; top: 110px; background: var(--card-front); }
  .brand {
    position: absolute; left: 40px; bottom: 70px;
    display: flex; align-items: center; gap: 14px;
  }
  .brand-mark {
    width: 54px; height: 54px; border-radius: 10px;
    background: var(--brand-red);
  }
  .brand-name {
    font-family: "Quicksand", sans-serif; font-weight: 500;
    font-size: 58px; color: var(--brand-grey); letter-spacing: 0.5px;
    line-height: 1;
  }

  /* Back side */
  .card-back { left: 550px; top: 520px; background: var(--card-back); overflow: hidden; }
  .back-strip {
    position: absolute; left: 0; right: 0; bottom: 0; height: 30px;
    background: var(--strip);
  }
  .back-rule {
    position: absolute; left: 245px; top: 40px; width: 2px; height: 205px;
    background: var(--rule);
  }
  .holder {
    position: absolute; left: 265px; top: 44px;
    color: var(--ink-light); font-family: "Arimo", sans-serif;
  }
  .holder-name {
    font-weight: 700; font-size: 30px; letter-spacing: 1.5px;
    margin-bottom: 26px;
  }
  .contact-list { list-style: none; font-size: 17px; line-height: 1.3; }
  .contact-gap { margin-top: 14px; }
</style>
</head>
<body>
<main class="canvas">
  <section class="card card-front" aria-label="Card front">
    <div class="brand">
      <span class="brand-mark" aria-hidden="true"></span>
      <span class="brand-name">Lomevu Linkup</span>
    </div>
  </section>

  <section class="card card-back" aria-label="Card back">
    <div class="back-rule"></div>
    <div class="holder">
      <h1 class="holder-name">TOBIN WEXMOOR</h1>
      <ul class="contact-list">
        <li>+468213579 (singapore)</li>
        <li>+315792846 (Australia)</li>
        <li>+729384615 (America)</li>
        <li class="contact-gap">www.lomevu-linkup.example</li>
        <li>ABN 86420913</li>
      </ul>
    </div>
    <div class="back-strip"></div>
  </section>
</main>
</body>
</html>
```